Brevik Plant Traders Company - Enhance our webpage

We have an existing website - please see www.brockwaytooling.com. The text in there is fundamentally what we want to say. There is also a search function where you can search our database, which is crucial to the site. We are happy with our logo, top left-hand side and want it to remain as it is. Everything else, including pictures, drawings and animation can be changed. In general, the website looks a little tired and the icons on the tabs need creative input.

We want our website to look dynamic, eye-catching, bold, very professional, modern and also uphold our impeccable 30-year reputation in the business.

We are essentially looking for a young, dynamic mind to provide our website with some inspiration. We encourage all designers to use their imagination and surprise us.

We have technical people to do the technical work, such as coding, but what we are looking for is asthetic creativity.

In addition, we have seen our competitors offer a translation service on their website i.e. you can just click on a flag and the website will turn into a different language. If you can incorporate this, it would be very useful.
Updates

Reason: Hi All - we have received some fantastic designs, so thank you. We are extending the deadline so that people can upgrade theirs slightly. We haven't seen enough dynamism with pictures and icons. And for those who have shown dynamism in those departments, we would also like you to consider including a video on the home page of some sort. You can find many videos of working machines like these on Clip-Spool. Thanks.

Target Market(s)

International Engineering companies

Industry/Entity Type

Flag

Requirements
Must have
• The "search database" facility must remain there.
Nice to have
• Perhaps some working videos running on the homepage of some of the types of machines we sell. You can find many such videos on ClipSpool. We will constantly change those as we get new stock in.

```html
<!DOCTYPE html>
<html lang="en">
<head>
<meta charset="utf-8">
<title>Brevik Plant Traders</title>
<link href="https://fonts.googleapis.com/css2?family=Questrial&family=Cabin:wght@400;600&display=swap" rel="stylesheet">
<style>
:root{
  --red:#e3000f;
  --black:#000;
  --ink:#222;
  --muted:#444;
  --page:#f3f3f3;
  --panel:#e4e4e4;
  --white:#fff;
  --line:#bbb;
}
*{box-sizing:border-box;margin:0;padding:0}
html,body{width:1200px;height:1014px;overflow:hidden;background:var(--page);font-family:"Cabin",sans-serif;color:var(--ink)}
.abs{position:absolute}
.brand{left:158px;top:6px;width:166px;height:83px;background:var(--red);display:flex;align-items:center;justify-content:center;text-align:center;color:var(--white);font-family:"Cabin",sans-serif;font-weight:600;font-size:21px;line-height:1.15;padding:0 8px}
.search-top{left:835px;top:16px;display:flex}
.search-top input{width:147px;height:23px;border:1px solid #ccc;background:#f8f8f8}
.search-top button{width:55px;height:23px;background:var(--black);color:var(--white);border:0;font-family:"Cabin",sans-serif;font-size:13px}
.nav{left:332px;top:56px;width:707px;height:33px;background:var(--black);display:flex;align-items:center;padding-left:21px;gap:0}
.nav a{color:var(--white);text-decoration:none;font-family:"Questrial",sans-serif;font-size:13.5px;margin-right:30px;white-space:nowrap}
.nav a:nth-child(3){margin-right:32px}
.content{left:157px;top:410px;width:886px;height:604px;background:var(--panel)}
.slider{left:157px;top:102px;width:886px;height:305px;background:var(--white);box-shadow:0 0 6px rgba(0,0,0,.25)}
.slide{left:16px;top:18px;width:854px;height:264px;background:linear-gradient(90deg,#6f6a63 0%,#8d8a80 25%,#9fc79c 50%,#5f6b74 75%,#4a4640 100%)}
.caption{right:0;bottom:15px;width:312px;height:53px;background:rgba(60,60,60,.55);color:var(--white);font-family:"Questrial",sans-serif;font-size:35px;display:flex;align-items:center;padding-left:23px}
.arrow{top:118px}
.dots{left:402px;top:289px;display:flex;gap:3px}
.dots span{width:8px;height:8px;border-radius:50%;background:var(--black)}
.dots span.on{background:var(--red)}
h2{font-family:"Questrial",sans-serif;font-weight:400;color:var(--red)}
.welcome-title{left:167px;top:425px;font-size:19px}
.welcome-img{left:169px;top:468px;width:127px;height:133px;background:linear-gradient(135deg,#8b7a64,#e4e2dc 45%,#c9c7c0)}
.welcome-text{left:313px;top:463px;width:435px;font-size:11.6px;line-height:20.3px;text-align:justify}
.card{width:288px;height:139px;background:var(--white);border:1px solid #ddd}
.card h2{position:absolute;left:13px;top:10px;width:167px;font-size:19px;padding-bottom:4px;border-bottom:1px solid var(--line)}
.card p{position:absolute;left:13px;top:50px;width:172px;font-size:10.5px;line-height:18.5px;color:var(--muted)}
.card .more{position:absolute;left:13px;top:114px;font-family:"Questrial",sans-serif;color:var(--red);font-size:16px}
.card .pic{position:absolute;left:207px;top:9px;width:90px;height:124px}
.pic-machine{background:linear-gradient(135deg,#8b7a64,#e6e4de 45%,#c4c2bb)}
.pic-grinder{background:linear-gradient(160deg,#5e8a5a,#9cbf8f 50%,#6d6d66)}
.pic-gears{background:linear-gradient(135deg,#dfe6ee,#4a6fa3 50%,#0e2f66)}
.newsletter{left:781px;top:422px;width:257px;height:143px;background:linear-gradient(135deg,#fafafa,#e8e8e8)}
.newsletter h2{position:absolute;left:18px;top:12px;font-size:19px}
.field{position:absolute;left:19px;width:225px;height:22px;border:1px solid #ccc;background:var(--white);font-size:11px;padding:4px 7px;color:#333}
.signup{position:absolute;left:189px;top:112px;width:52px;height:23px;background:var(--red);color:var(--white);font-size:11.5px;display:flex;align-items:center;justify-content:center}
.finder{left:780px;top:574px;width:258px;height:138px;background:var(--white)}
.finder p{position:absolute;left:12px;top:14px;width:234px;text-align:center;font-size:11.3px;line-height:19px}
.finder .field{left:14px;top:69px;width:233px;height:26px;font-size:10px;color:#777;padding-top:6px}
.go{position:absolute;left:205px;top:96px;font-family:"Questrial",sans-serif;font-size:32px;color:var(--red);line-height:1}
.contact{left:780px;top:733px;width:258px;height:159px;background:var(--white)}
.contact h2{position:absolute;left:15px;top:12px;width:180px;font-size:19px;padding-bottom:3px;border-bottom:1px solid var(--line)}
.contact .info{position:absolute;left:16px;top:52px;font-size:11.3px;line-height:20.5px}
.contact .info span{color:var(--red)}
.headset{position:absolute;left:200px;top:12px}
.footer{left:166px;top:943px;width:870px;height:58px;background:var(--white);text-align:center;font-size:10.6px;color:#333;padding-top:9px;line-height:19px}
</style>
</head>
<body>
<div class="abs brand">Brevik Plant Traders</div>
<form class="abs search-top"><input type="text" aria-label="Search"><button type="button">Search</button></form>
<nav class="abs nav">
  <a>HOME</a><a>NEW CNC MACHINES</a><a>USED MACHINES</a><a>MANUFACTURING</a><a>CONTACT</a><a>ABOUT US</a>
</nav>

<div class="abs content"></div>

<section class="abs slider">
  <div class="abs slide" role="img" aria-label="Photo of a large CNC vertical turning lathe in a workshop">
    <svg class="abs arrow" style="left:16px" width="20" height="30" viewBox="0 0 20 30"><path d="M16 3 L5 15 L16 27" fill="none" stroke="#fff" stroke-width="4"/></svg>
    <svg class="abs arrow" style="right:16px" width="20" height="30" viewBox="0 0 20 30"><path d="M4 3 L15 15 L4 27" fill="none" stroke="#fff" stroke-width="4"/></svg>
    <div class="abs caption">CNC Korvan VTL</div>
  </div>
  <div class="abs dots"><span></span><span class="on"></span><span></span><span></span><span></span></div>
</section>

<h2 class="abs welcome-title">WELCOME TO OUR SITE</h2>
<div class="abs welcome-img" role="img" aria-label="Photo of an enclosed CNC machine with control panel"></div>
<p class="abs welcome-text">Brevik Plant Traders is an established vendor of new and used machine tools, with over 30 years' experience in buying, rebuilding, retrofitting and commissioning machine tools WORLDWIDE. We have industrial space both in London and Mumbai, where we store over 200 machines at any given time. We specialise in gear manufacturing, pressure diecasting, plano miller, boring and grinding machines, as well as heat treatment facilities, machining and turning centres. Such machines find their usage in the automotive, aviation, power generation, mining and construction industries.</p>

<article class="abs card" style="left:167px;top:639px">
  <h2>new cnc machines</h2>
  <p>We understand our customers' growing need for CNC technology in their machine tools.</p>
  <span class="more">more</span>
  <div class="pic pic-machine" role="img" aria-label="Photo of a new CNC machine"></div>
</article>
<article class="abs card" style="left:462px;top:639px">
  <h2>used machines</h2>
  <p>Boltmakers , Borers All Types , Broach Grinder / Broach Sharpner, Broaching machines...</p>
  <span class="more">more</span>
  <div class="pic pic-machine" role="img" aria-label="Photo of a used machine tool"></div>
</article>
<article class="abs card" style="left:167px;top:786px">
  <h2>used gear grinder</h2>
  <p>We understand our customers' growing need for CNC technology in their machine tools.</p>
  <span class="more">more</span>
  <div class="pic pic-grinder" role="img" aria-label="Photo of a green gear grinding machine"></div>
</article>
<article class="abs card" style="left:462px;top:786px">
  <h2>Manufacturing</h2>
  <p>We have a manufacturing arm in Mumbai, India, where we produce gears from 16mm to 1600mm..</p>
  <span class="more">more</span>
  <div class="pic pic-gears" role="img" aria-label="Illustration of interlocking steel gears"></div>
</article>

<aside class="abs newsletter">
  <h2>newsletter signup</h2>
  <div class="field" style="top:51px">Enter the name</div>
  <div class="field" style="top:82px">Enter the E mail id</div>
  <div class="signup">SIGN UP</div>
</aside>

<aside class="abs finder">
  <p>Please use this search bar to browse our entire global stocklist - just type in any keyword!</p>
  <div class="field">Type Any Machine Name</div>
  <div class="go">g<svg width="20" height="20" viewBox="0 0 20 20" style="vertical-align:-2px"><circle cx="10" cy="10" r="10" fill="#e3000f"/></svg></div>
</aside>

<aside class="abs contact">
  <h2>contact us</h2>
  <svg class="headset" width="48" height="52" viewBox="0 0 48 52" aria-hidden="true">
    <path d="M8 28 C8 10 40 10 40 28" fill="none" stroke="#333" stroke-width="3"/>
    <rect x="4" y="24" width="9" height="15" rx="3" fill="#222"/>
    <rect x="35" y="24" width="9" height="15" rx="3" fill="#222"/>
    <path d="M9 39 C9 46 14 48 18 48" fill="none" stroke="#333" stroke-width="2"/>
  </svg>
  <div class="info">
    14-16 Mill Lane, Harrowfield, HF2 7QT,<br>
    United Kingdom<br>
    Tel. : <span>0044-0201-555-0142</span><br>
    Fax : <span>0044-0201-555-0187</span><br>
    Email : sales@brockwaytooling.com
  </div>
</aside>

<footer class="abs footer">
  Home | About Us | Used Machines | Manufacturing | New CNC Machines | Enquiry | Contact Us | Sitemap<br>
  Copyright. Brevik Plant Traders. All Rights Reserved
</footer>
</body>
</html>
```